Security Warning Sign

We have an existing sign that needs an update. I have attached a picture of the current square sign. We need to maintain the same wording. It needs to be professional and appropriate to attach to our customers fence. Also attached is a copy of our building sign which may lend some inspiration and hopefully the ai format will assist. The final sign will be 600mm x 600mmOur website is www.halvorngate.com.au

```html
<!DOCTYPE html>
<html lang="en">
<head>
<meta charset="utf-8">
<title>Halvorngate Security Services – Surveillance Warning Sign</title>
<link rel="stylesheet" href="https://fonts.googleapis.com/css2?family=Open+Sans:wght@800&family=Roboto+Condensed:wght@700&display=swap">
<style>
  :root {
    --orange: #f38634;
    --ink: #1b1b1b;
    --white: #ffffff;
    --bg-light: #fafafa;
    --bg-shade: #e6e7e8;
  }
  html, body {
    margin: 0;
    padding: 0;
    width: 1200px;
    height: 1200px;
    overflow: hidden;
    background: var(--white);
  }
  .sign {
    display: block;
    width: 1200px;
    height: 1200px;
  }
  .headline {
    font-family: "Open Sans", Arial, sans-serif;
    font-weight: 800;
    font-size: 198px;
    fill: var(--orange);
  }
  .notice {
    font-family: "Open Sans", Arial, sans-serif;
    font-weight: 800;
    font-size: 88px;
    fill: var(--ink);
  }
  .brand-name {
    font-family: "Open Sans", Arial, sans-serif;
    font-weight: 800;
    font-size: 37px;
    fill: var(--white);
  }
  .phone {
    font-family: "Roboto Condensed", "Arial Narrow", sans-serif;
    font-weight: 700;
    font-size: 100px;
    fill: var(--white);
  }
</style>
</head>
<body>
<svg class="sign" viewBox="0 0 1200 1200" xmlns="http://www.w3.org/2000/svg">
  <defs>
    <linearGradient id="panel-shade" x1="0" y1="0" x2="1" y2="1">
      <stop offset="0" stop-color="var(--bg-light)"/>
      <stop offset="0.5" stop-color="var(--bg-shade)"/>
      <stop offset="1" stop-color="var(--bg-light)"/>
    </linearGradient>
  </defs>

  <rect class="background" role="img" aria-label="Soft grey faceted low-poly background" x="0" y="0" width="1200" height="1200" fill="url(#panel-shade)"/>

  <text class="headline" x="104" y="263" textLength="994" lengthAdjust="spacingAndGlyphs">WARNING</text>

  <g class="notice-block" text-anchor="middle">
    <text class="notice" x="600" y="436" textLength="546" lengthAdjust="spacingAndGlyphs">ELECTRONIC</text>
    <text class="notice" x="600" y="550" textLength="888" lengthAdjust="spacingAndGlyphs">SURVEILLANCE AND</text>
    <text class="notice" x="600" y="663" textLength="522" lengthAdjust="spacingAndGlyphs">RECORDING</text>
    <text class="notice" x="600" y="775" textLength="862" lengthAdjust="spacingAndGlyphs">DEVICES INSTALLED</text>
    <text class="notice" x="600" y="888" textLength="586" lengthAdjust="spacingAndGlyphs">IN THIS AREA</text>
  </g>

  <g class="footer-band">
    <polygon class="brand-panel" points="0,959 596,959 451,1200 0,1200" fill="var(--ink)"/>
    <polygon class="accent-stripe" points="562,1031 575,1031 458,1200 445,1200" fill="var(--orange)"/>
    <polygon class="phone-panel" points="588,1031 1200,1031 1200,1200 487,1200" fill="var(--orange)"/>
  </g>

  <g class="brand">
    <circle class="brand-mark" cx="144" cy="1094" r="66" fill="var(--orange)"/>
    <text class="brand-name" x="232" y="1057" textLength="262" lengthAdjust="spacingAndGlyphs">HALVORNGATE</text>
    <text class="brand-name" x="232" y="1096" textLength="188" lengthAdjust="spacingAndGlyphs">SECURITY</text>
    <text class="brand-name" x="232" y="1134" textLength="180" lengthAdjust="spacingAndGlyphs">SERVICES</text>
  </g>

  <text class="phone" x="624" y="1158" textLength="508" lengthAdjust="spacingAndGlyphs">1300 555 018</text>
</svg>
</body>
</html>
```